Create a business promotion flyer to leave in customer mailboxes. We are a bulk petroleum supplier, servicing any industry that requires diesel. Base in griffith NSW, servicing griffith area and surrounds.

Business Name - Terra Petro
Fuel@terrapetro-example.com.au
Marco - 0400 000 001 mtorrisi@terrapetro-example.com.au
Liam - 0400 000 002 lharcourt@terrapetro-example.com.au
Peter - 0400 000 003 pwinslow@terrapetro-example.com.au
Office 02 5550 0100

Bulk Fuel deliveries.
Oils & lubricants
Local Family owned business

```html
<!DOCTYPE html>
<html lang="en">
<head>
<meta charset="utf-8">
<title>Terra Petro – Bulk Fuel Flyer</title>
<link href="https://fonts.googleapis.com/css2?family=Montserrat:ital,wght@0,400;0,500;0,600;0,700;0,800;1,800&family=Great+Vibes&display=swap" rel="stylesheet">
<style>
  :root{
    --red:#e52521;
    --charcoal:#1f1f20;
    --ink:#333;
    --grey:#6b6c6f;
    --text-grey:#555;
    --light-line:#dcdcdc;
    --page:#e9e9e9;
    --white:#fff;
  }
  *{box-sizing:border-box;margin:0;padding:0}
  html,body{width:1200px;height:2407px;overflow:hidden;background:var(--page)}
  body{font-family:'Montserrat',sans-serif;color:var(--ink);position:relative}

  .flyer{
    position:absolute;left:60px;top:506px;
    width:835px;height:1078px;background:var(--white);
    transform:scale(1.2934);transform-origin:top left;
    box-shadow:0 6px 18px rgba(0,0,0,.18);
    overflow:hidden;
  }

  /* header */
  .brand{position:absolute;left:50px;top:82px;display:flex;align-items:center;gap:10px;white-space:nowrap}
  .brand-dot{width:24px;height:24px;border-radius:50%;background:var(--red)}
  .brand-name{font-size:30px;font-weight:600;color:var(--red);letter-spacing:-.3px}
  .headline{position:absolute;left:305px;top:46px;font-weight:800;font-style:italic;font-size:34px;line-height:44px;letter-spacing:-.3px;white-space:nowrap}
  .headline .line-red{color:var(--red)}
  .headline .line-grey{color:#505154}

  /* hero */
  .hero-photo{
    position:absolute;left:0;top:133px;width:835px;height:420px;
    background:linear-gradient(180deg,#7fa6cf 0%,#c6d3df 28%,#a4a9ae 55%,#8a8d90 80%,#77797b 100%);
  }
  .hero-swoosh{position:absolute;left:0;top:430px;width:835px;height:180px}

  .badge{
    position:absolute;left:44px;top:348px;width:182px;height:182px;border-radius:50%;
    background:var(--grey);border:4px solid var(--white);
    box-shadow:0 5px 10px rgba(0,0,0,.35);
    color:var(--white);text-align:center;
    display:flex;flex-direction:column;align-items:center;justify-content:center;
  }
  .badge-small{font-size:12px;font-weight:600;line-height:14px}
  .badge-town{font-size:21px;font-weight:800;line-height:24px}
  .badge-rule{width:116px;height:1.5px;background:var(--white);margin:6px 0 8px}
  .badge-serv{font-size:12px;font-weight:700;line-height:15px}

  /* intro */
  .intro{position:absolute;left:0;top:578px;width:835px;text-align:center;font-size:16px;line-height:22px;color:#444}
  .intro strong{color:var(--red);font-weight:700}

  /* services */
  .services{position:absolute;left:0;top:638px;width:835px;height:180px;display:flex}
  .service{flex:0 0 auto;text-align:center;display:flex;flex-direction:column;align-items:center}
  .service:nth-child(1){width:268px;padding-left:24px}
  .service:nth-child(2){width:275px;border-left:1px solid var(--light-line);border-right:1px solid var(--light-line)}
  .service:nth-child(3){width:292px}
  .service-icon{width:66px;height:66px;border-radius:50%;background:var(--red);display:flex;align-items:center;justify-content:center}
  .service-title{margin-top:14px;font-size:18px;font-weight:800;line-height:23px;color:#2a2a2a}
  .service-text{margin-top:10px;font-size:12.5px;line-height:16px;color:var(--text-grey)}

  /* contacts */
  .contacts{position:absolute;left:0;top:832px;width:835px;height:114px;background:var(--charcoal);display:flex;padding-top:20px}
  .contact{flex:0 0 auto}
  .contact:nth-child(1){width:276px;padding-left:36px}
  .contact:nth-child(2){width:285px;padding-left:24px;border-left:1px solid var(--red)}
  .contact:nth-child(3){width:274px;padding-left:22px;border-left:1px solid var(--red)}
  .contact-name{color:var(--red);font-size:18px;font-weight:800;line-height:22px;text-transform:uppercase}
  .contact:nth-child(3) .contact-name{text-transform:none}
  .contact-row{display:flex;align-items:center;gap:8px;color:var(--white);font-size:10.5px;line-height:22px;white-space:nowrap}
  .contact-row svg{flex:0 0 auto}

  .office-bar{position:absolute;left:0;top:946px;width:835px;height:47px;background:var(--red);display:flex;align-items:center;color:var(--white);font-size:12.5px;white-space:nowrap}
  .office-label{font-size:18px;font-weight:800;margin-left:36px;width:96px}
  .office-item{display:flex;align-items:center;gap:8px;flex:0 0 auto}
  .office-item.phone{width:140px}
  .office-item.email{width:255px}

  /* footer */
  .footer{position:absolute;left:66px;top:1010px;display:flex;align-items:center;gap:16px}
  .footer-script{font-family:'Great Vibes',cursive;color:var(--red);font-size:38px}
  .footer-values{font-size:14px;color:#444;letter-spacing:.2px;word-spacing:4px}
</style>
</head>
<body>
<main class="flyer">

  <header>
    <div class="brand">
      <span class="brand-dot"></span>
      <span class="brand-name">Terra Petro</span>
    </div>
    <h1 class="headline">
      <span class="line-red">FUELLING YOUR BUSINESS.</span><br>
      <span class="line-grey">KEEPING YOU MOVING.</span>
    </h1>
  </header>

  <section class="hero">
    <div class="hero-photo" role="img" aria-label="Photo of a white fuel tanker road train parked outside a large steel depot shed under a blue sky"></div>
    <svg class="hero-swoosh" viewBox="0 0 835 180" preserveAspectRatio="none">
      <path d="M0,61 C250,0 560,10 835,43 L835,85 C560,60 250,90 0,163 Z" fill="var(--red)"/>
      <path d="M0,163 C250,90 560,60 835,85 L835,180 L0,180 Z" fill="var(--white)"/>
    </svg>
    <div class="badge">
      <div class="badge-small">BASED IN</div>
      <div class="badge-town">GRIFFITH</div>
      <div class="badge-small">NSW</div>
      <div class="badge-rule"></div>
      <div class="badge-serv">SERVICING<br>GRIFFITH AREA<br>&amp; SURROUNDS</div>
    </div>
  </section>

  <p class="intro">Terra Petro is your <strong>reliable local</strong> partner for bulk diesel supply.<br>We deliver when you need it, where you need it.</p>

  <section class="services">
    <article class="service">
      <div class="service-icon">
        <svg width="38" height="38" viewBox="0 0 38 38" fill="none" stroke="#fff" stroke-width="2" stroke-linejoin="round" stroke-linecap="round">
          <path d="M5 13 L20 6 L33 22 L26 30 Z"/>
          <path d="M12 10 L8 4"/>
          <path d="M26 30 L30 35"/>
          <path d="M14 17 L22 26"/>
        </svg>
      </div>
      <h2 class="service-title">BULK FUEL<br>DELIVERIES</h2>
      <p class="service-text">Quality diesel, delivered<br>safely and on time.</p>
    </article>
    <article class="service">
      <div class="service-icon">
        <svg width="38" height="38" viewBox="0 0 38 38" fill="none" stroke="#fff" stroke-width="2" stroke-linejoin="round">
          <path d="M19 4 C19 4 11 14 11 19 a8 8 0 0 0 16 0 C27 14 19 4 19 4 Z"/>
          <path d="M8 27 a12 8 0 0 0 22 0" stroke-dasharray="3 2"/>
        </svg>
      </div>
      <h2 class="service-title">OILS &amp;<br>LUBRICANTS</h2>
      <p class="service-text">Premium oils and lubricants<br>to keep your equipment<br>performing at its best.</p>
    </article>
    <article class="service">
      <div class="service-icon">
        <svg width="36" height="36" viewBox="0 0 36 36" fill="none" stroke="#fff" stroke-width="2" stroke-linejoin="round">
          <path d="M18 33 C18 33 7 21 7 14 a11 11 0 0 1 22 0 C29 21 18 33 18 33 Z"/>
          <circle cx="18" cy="14" r="4"/>
        </svg>
      </div>
      <h2 class="service-title">LOCAL FAMILY<br>OWNED BUSINESS</h2>
      <p class="service-text">Proudly supporting our local<br>community with honest<br>service and strong values.</p>
    </article>
  </section>

  <section class="contacts">
    <div class="contact">
      <div class="contact-name">Marco</div>
      <div class="contact-row"><svg width="13" height="13" viewBox="0 0 24 24" fill="none" stroke="#e52521" stroke-width="2"><path d="M5 3h4l2 5-3 2a12 12 0 0 0 6 6l2-3 5 2v4a2 2 0 0 1-2 2A18 18 0 0 1 3 5a2 2 0 0 1 2-2z"/></svg>0400 000 001</div>
      <div class="contact-row"><svg width="13" height="11" viewBox="0 0 24 18" fill="none" stroke="#e52521" stroke-width="2"><rect x="1" y="1" width="22" height="16"/><path d="M1 1l11 9 11-9"/></svg>mtorrisi@terrapetro-example.com.au</div>
    </div>
    <div class="contact">
      <div class="contact-name">Liam</div>
      <div class="contact-row"><svg width="13" height="13" viewBox="0 0 24 24" fill="none" stroke="#e52521" stroke-width="2"><path d="M5 3h4l2 5-3 2a12 12 0 0 0 6 6l2-3 5 2v4a2 2 0 0 1-2 2A18 18 0 0 1 3 5a2 2 0 0 1 2-2z"/></svg>0400 000 002</div>
      <div class="contact-row"><svg width="13" height="11" viewBox="0 0 24 18" fill="none" stroke="#e52521" stroke-width="2"><rect x="1" y="1" width="22" height="16"/><path d="M1 1l11 9 11-9"/></svg>lharcourt@terrapetro-example.com.au</div>
    </div>
    <div class="contact">
      <div class="contact-name">Peter</div>
      <div class="contact-row"><svg width="13" height="13" viewBox="0 0 24 24" fill="none" stroke="#e52521" stroke-width="2"><path d="M5 3h4l2 5-3 2a12 12 0 0 0 6 6l2-3 5 2v4a2 2 0 0 1-2 2A18 18 0 0 1 3 5a2 2 0 0 1 2-2z"/></svg>0400 000 003</div>
      <div class="contact-row"><svg width="13" height="11" viewBox="0 0 24 18" fill="none" stroke="#e52521" stroke-width="2"><rect x="1" y="1" width="22" height="16"/><path d="M1 1l11 9 11-9"/></svg>pwinslow@terrapetro-example.com.au</div>
    </div>
  </section>

  <section class="office-bar">
    <span class="office-label">OFFICE</span>
    <span class="office-item phone"><svg width="15" height="15" viewBox="0 0 24 24" fill="none" stroke="#fff" stroke-width="2"><path d="M5 3h4l2 5-3 2a12 12 0 0 0 6 6l2-3 5 2v4a2 2 0 0 1-2 2A18 18 0 0 1 3 5a2 2 0 0 1 2-2z"/></svg>02 5550 0100</span>
    <span class="office-item email"><svg width="15" height="12" viewBox="0 0 24 18" fill="none" stroke="#fff" stroke-width="2"><rect x="1" y="1" width="22" height="16"/><path d="M1 1l11 9 11-9"/></svg>Fuel@terrapetro-example.com.au</span>
    <span class="office-item web"><svg width="15" height="15" viewBox="0 0 24 24" fill="none" stroke="#fff" stroke-width="2"><circle cx="12" cy="12" r="10"/><ellipse cx="12" cy="12" rx="4" ry="10"/><path d="M2 12h20"/></svg>www.terrapetro-example.com.au</span>
  </section>

  <footer class="footer">
    <span class="footer-script">We deliver</span>
    <span class="footer-values">RELIABILITY. SAFETY. QUALITY. EVERY TIME.</span>
  </footer>

</main>
</body>
</html>
```